Looking for a clean, modern, and professional business card design that reflects Valtrim Systems

The design should include the company logo, contact details, and align with our brand identity. Please use a sophisticated and minimalist style, incorporating [specific colors, if applicable]. Creativity is welcome, but the card must maintain a polished and professional appearance.

Details to Include:

Name: Gavin Trelowe
Title: VP Sales / Operations
Company: Valtrim Systems
Phone: 483.216.7705
Email: gavin@valtrimsystems-example.com
Website: www.valtrimsystems-example.com

```html
<!DOCTYPE html>
<html lang="en">
<head>
<meta charset="utf-8">
<title>Valtrim Systems — Business Card</title>
<link href="https://fonts.googleapis.com/css2?family=Lato:wght@400;700;900&display=swap" rel="stylesheet">
<style>
  :root {
    --backdrop: #3d3d3d;
    --card-white: #ffffff;
    --card-black: #161616;
    --card-black-soft: #2a2a2a;
    --brand-blue: #3a78c0;
    --ink: #1a1a1a;
    --ink-soft: #2b2b2b;
    --rule: #6a6a6a;
  }
  * { box-sizing: border-box; margin: 0; padding: 0; }
  html, body {
    width: 1200px;
    height: 803px;
    overflow: hidden;
    background: var(--backdrop);
    font-family: "Lato", Arial, sans-serif;
  }
  .stage {
    position: relative;
    width: 1200px;
    height: 803px;
  }
  .card {
    position: absolute;
    width: 525px;
    height: 300px;
    border-radius: 22px;
    box-shadow: 0 14px 30px rgba(0,0,0,0.35);
    overflow: hidden;
  }
  .card-front {
    left: 60px;
    top: 110px;
    background: var(--card-white);
  }
  .card-back {
    left: 615px;
    top: 393px;
    background: var(--card-black);
  }

  /* Front: brand block */
  .brand {
    position: absolute;
    left: 38px;
    top: 0;
    height: 100%;
    width: 220px;
    display: flex;
    align-items: center;
    gap: 10px;
  }
  .brand-dot {
    width: 14px;
    height: 14px;
    border-radius: 50%;
    background: var(--brand-blue);
    flex: none;
  }
  .brand-name {
    font-weight: 900;
    font-size: 25px;
    letter-spacing: 0.5px;
    color: var(--ink);
    line-height: 1.1;
    text-transform: uppercase;
  }

  .divider {
    position: absolute;
    left: 262px;
    top: 78px;
    width: 1px;
    height: 144px;
    background: linear-gradient(to bottom, transparent, var(--rule) 30%, var(--rule) 70%, transparent);
  }

  /* Front: contact block */
  .contact {
    position: absolute;
    left: 282px;
    top: 86px;
    right: 20px;
  }
  .person-name {
    font-weight: 700;
    font-size: 21px;
    color: var(--brand-blue);
    line-height: 1.1;
  }
  .person-title {
    font-size: 13px;
    color: var(--ink-soft);
    margin-top: 3px;
  }
  .details {
    list-style: none;
    margin-top: 18px;
  }
  .details li {
    display: flex;
    align-items: center;
    gap: 7px;
    font-size: 11.5px;
    color: var(--ink-soft);
    line-height: 1.6;
    white-space: nowrap;
  }
  .details svg {
    width: 11px;
    height: 11px;
    flex: none;
    fill: var(--brand-blue);
  }

  /* Back: textured surface */
  .back-texture {
    position: absolute;
    inset: 0;
    background:
      radial-gradient(ellipse at 75% 25%, #5a5a5a 0%, rgba(60,60,60,0.6) 25%, transparent 60%),
      linear-gradient(135deg, var(--card-black) 0%, var(--card-black-soft) 55%, #3a3a3a 100%);
  }
  .back-mark {
    position: absolute;
    left: 50%;
    top: 50%;
    width: 16px;
    height: 16px;
    margin: -8px 0 0 -8px;
    border-radius: 50%;
    background: var(--brand-blue);
  }
</style>
</head>
<body>
<main class="stage">
  <section class="card card-front" aria-label="Business card front">
    <div class="brand">
      <span class="brand-dot"></span>
      <span class="brand-name">Valtrim Systems</span>
    </div>
    <div class="divider"></div>
    <div class="contact">
      <p class="person-name">Gavin Trelowe</p>
      <p class="person-title">VP Sales / Operations</p>
      <ul class="details">
        <li>
          <svg viewBox="0 0 24 24" aria-hidden="true"><path d="M6.6 10.8a15.1 15.1 0 0 0 6.6 6.6l2.2-2.2a1 1 0 0 1 1-.25 11.4 11.4 0 0 0 3.6.57 1 1 0 0 1 1 1V20a1 1 0 0 1-1 1A17 17 0 0 1 3 4a1 1 0 0 1 1-1h3.5a1 1 0 0 1 1 1c0 1.25.2 2.46.57 3.6a1 1 0 0 1-.25 1z"/></svg>
          483.216.7705
        </li>
        <li>
          <svg viewBox="0 0 24 24" aria-hidden="true"><path d="M2 5h20v14H2z M2 5l10 8 10-8" /></svg>
          gavin@valtrimsystems-example.com
        </li>
        <li>
          <svg viewBox="0 0 24 24" aria-hidden="true"><path d="M12 2a10 10 0 1 0 0 20 10 10 0 0 0 0-20zm0 2.2a7.8 7.8 0 0 1 7.8 7.8A7.8 7.8 0 1 1 12 4.2z M11 6h2v12h-2z M6 11h12v2H6z"/></svg>
          www.valtrimsystems-example.com
        </li>
      </ul>
    </div>
  </section>

  <section class="card card-back" aria-label="Business card back">
    <div class="back-texture" role="img" aria-label="Black card surface with a repeating embossed pattern in glossy greys"></div>
    <span class="back-mark"></span>
  </section>
</main>
</body>
</html>
```